New website

Our website (www.larchvale.com) needs to be replaced with something gorgeous and glossy. We do like the text of our current website but have many new images to put on the site. We want to create a website that shows viewers what our team can do, and how we can create something amazing for them and their homes.

Coding

```html
<!DOCTYPE html>
<html lang="en">
<head>
<meta charset="utf-8">
<title>Larchvale Landscaping</title>
<link href="https://fonts.googleapis.com/css2?family=Sora:wght@400;500;600;700&family=Inter:wght@400;500;600&display=swap" rel="stylesheet">
<style>
:root{
  --green:#6cb425;
  --green-dark:#4f8f14;
  --ink:#1c1c1c;
  --muted:#7a7a7a;
  --cream:#f6f2ec;
  --white:#ffffff;
  --dark:#1b1d19;
  --line:#e6e1d8;
}
*{margin:0;padding:0;box-sizing:border-box}
html,body{width:1200px;height:4971px;overflow:hidden}
body{position:relative;font-family:"Inter",sans-serif;color:var(--ink);background:var(--white)}
.abs{position:absolute}
h1,h2,h3,h4,.head{font-family:"Sora",sans-serif;color:var(--ink)}
p{font-size:12.5px;line-height:18px;color:var(--muted)}
.btn{position:absolute;display:flex;align-items:center;justify-content:center;background:var(--green);color:#fff;font-family:"Sora",sans-serif;font-size:12px;font-weight:600;border-radius:3px}
.eyebrow{position:absolute;font-family:"Sora",sans-serif;font-size:11.5px;font-weight:600;color:var(--green)}
.photo{position:absolute}
.deco{position:absolute;border-radius:50%;background:radial-gradient(circle,#9fd35a 0%,#6cb42566 60%,transparent 72%)}

/* top header */
.header-card{left:73px;top:36px;width:1052px;height:118px;background:#fff}
.topbar{left:104px;top:46px;font-size:12px;display:flex;gap:26px;color:var(--ink);align-items:center}
.topbar span{display:flex;align-items:center;gap:6px}
.socials{left:940px;top:44px;display:flex;gap:14px}
.socials i{width:22px;height:22px;border-radius:50%;background:var(--ink);display:block}
.divider{left:73px;top:76px;width:1052px;height:1px;background:var(--line)}
.brand{left:104px;top:98px;font-family:"Sora",sans-serif;font-size:27px;font-weight:500;letter-spacing:5px;color:#2c2c2c;display:flex;align-items:center;gap:10px}
.brand b{width:14px;height:14px;background:var(--green);border-radius:50%;display:block}
.nav{left:468px;top:108px;display:flex;gap:48px;font-family:"Sora",sans-serif;font-size:11.5px;font-weight:600}

/* hero */
.hero{left:0;top:0;width:1200px;height:749px;background:var(--cream);z-index:-1}
.hero h1{left:104px;top:300px;font-size:48px;line-height:56px;font-weight:600;position:absolute}
.hero-text{left:104px;top:424px;width:480px}

/* features */
.feature{position:absolute;top:838px;width:240px;text-align:center}
.icon-ring{width:58px;height:58px;border-radius:50%;border:1.5px solid #cfe5b5;margin:0 auto;display:flex;align-items:center;justify-content:center}
.feature h3{font-size:15px;font-weight:600;margin-top:30px}
.feature p{font-size:11.5px;margin-top:6px}

/* about */
.about-bg{left:0;top:1077px;width:1200px;height:575px;background:var(--cream)}
.sec-title{position:absolute;font-size:27px;line-height:36px;font-weight:600}
.checks{position:absolute;display:grid;grid-template-columns:193px 193px;row-gap:13px;font-size:12px;color:var(--muted)}
.checks span{display:flex;align-items:center;gap:8px}
.checks span:before{content:"";width:11px;height:11px;background:var(--green);border-radius:2px}
.stat-mini{position:absolute;display:flex;gap:14px;align-items:center}
.stat-mini .icon-ring{width:54px;height:54px;margin:0}
.stat-mini strong{display:block;font-family:"Sora",sans-serif;color:var(--green);font-size:18px}
.stat-mini em{font-style:normal;font-family:"Sora",sans-serif;font-size:14px;font-weight:600}

/* services */
.service{position:absolute;width:236px}
.service .icon-ring{margin:0;width:56px;height:56px}
.service h3{font-size:14.5px;font-weight:600;margin-top:20px}
.service p{font-size:11.5px;line-height:17px;margin-top:6px}
.service a{display:block;margin-top:10px;font-family:"Sora",sans-serif;font-size:11px;font-weight:700;color:var(--ink);text-decoration:none}

/* counters */
.counters{left:0;top:2476px;width:1200px;height:322px;background:linear-gradient(180deg,#22261d,#15170f)}
.counter{position:absolute;top:2564px;width:200px;text-align:center;color:#fff}
.counter .icon-ring{width:76px;height:76px;border-color:var(--green)}
.counter strong{display:block;font-family:"Sora",sans-serif;font-size:24px;margin-top:12px}
.counter span{font-size:12.5px}

/* team */
.center{position:absolute;left:0;width:1200px;text-align:center}
.member{position:absolute;top:3036px;width:234px;height:303px;background:#f3f0ea}
.member .photo{left:0;top:0;width:234px;height:235px}
.member .share{position:absolute;right:14px;top:14px;width:26px;height:26px;background:#222;border-radius:3px}
.member h4{position:absolute;top:256px;width:100%;text-align:center;font-size:14.5px;font-weight:600}
.member span{position:absolute;top:278px;width:100%;text-align:center;font-size:11.5px;color:var(--muted)}

/* testimonials */
.testi-bg{left:600px;top:3522px;width:600px;height:743px;background:var(--cream)}
.review{position:absolute;left:641px;width:453px;background:#fff;padding:28px 32px}
.review .who{display:flex;align-items:center;gap:14px}
.avatar{width:58px;height:58px;border-radius:50%;background:linear-gradient(135deg,#8aa36b,#4d5c3a)}
.review h4{font-size:14px;font-weight:600}
.review small{font-size:11px;color:var(--muted)}
.stars{margin-left:auto;color:var(--green);font-size:13px;letter-spacing:1px}
.review p{margin-top:24px;font-size:11.5px}

/* partners */
.badge{position:absolute;top:4336px;width:110px;height:70px;border-radius:50%;background:#eef3e4}

/* footer */
.footer-bg{left:0;top:4478px;width:1200px;height:493px;background:var(--cream)}
.footer h4{position:absolute;top:4622px;font-size:15px;font-weight:600}
.links{position:absolute;left:400px;top:4664px;list-style:none;font-size:12.5px;line-height:31.5px}
.links li{display:flex;align-items:center;gap:10px}
.links li:before{content:"";width:10px;height:8px;background:var(--green);border-radius:0 6px 0 6px}
.news{position:absolute;left:608px;display:flex;gap:16px}
.news .photo{position:relative;width:70px;height:70px}
.news b{display:block;font-family:"Sora",sans-serif;font-size:11.5px;line-height:17px;width:150px}
.news span{font-size:11px;color:var(--green)}
.gallery{position:absolute;left:861px;top:4664px;display:grid;grid-template-columns:repeat(3,72px);gap:8px}
.gallery div{height:70px;background:linear-gradient(135deg,#78925a,#3e4d2f)}
.copy{top:4930px;font-size:12px;color:var(--muted)}
.copy-line{left:104px;top:4908px;width:990px;height:1px;background:#e1dbd0}
</style>
</head>
<body>

<!-- Hero -->
<div class="abs hero"></div>
<div class="abs header-card"></div>
<div class="abs topbar">
  <span><svg width="12" height="12" viewBox="0 0 24 24"><path d="M6 2l4 4-2 3a12 12 0 006 6l3-2 4 4-3 3C9 20 4 15 3 5z" fill="var(--green)"/></svg>(555) 204-7781</span>
  <span><svg width="12" height="12" viewBox="0 0 24 24"><circle cx="12" cy="12" r="9" fill="none" stroke="var(--green)" stroke-width="2.5"/></svg>info@larchvale.com</span>
  <span style="margin-left:12px"><svg width="12" height="14" viewBox="0 0 24 28"><path d="M12 1a9 9 0 019 9c0 7-9 17-9 17S3 17 3 10a9 9 0 019-9z" fill="var(--green)"/><circle cx="12" cy="10" r="3" fill="#fff"/></svg>418 Hollow Birch Rd, Fernwick, MI 49000</span>
</div>
<div class="abs socials"><i></i><i></i><i></i><i></i></div>
<div class="abs divider"></div>
<div class="abs brand"><b></b>LARCHVALE</div>
<nav class="abs nav"><span>HOME</span><span>ABOUT US</span><span>SERVICES</span><span>TESTIMONIALS</span><span>CONTACT</span></nav>
<div class="btn" style="left:991px;top:93px;width:104px;height:40px">Get A Quote</div>

<section class="hero">
  <h1>Experts For All<br>Seasons</h1>
  <p class="abs hero-text">Established in 2005 as a way to pay for college tuition, Larchvale has instead become our passion. With a garage sale mower and a commitment to doing every job well, our list of satisfied customers grew quickly over the years.</p>
</section>
<div class="btn" style="left:104px;top:508px;width:116px;height:39px">Learn More</div>
<div class="btn" style="left:243px;top:508px;width:116px;height:39px">Learn More</div>
<div class="photo" role="img" aria-label="Gardener in blue gloves potting a small plant" style="left:724px;top:266px;width:434px;height:390px;border-radius:48% 52% 45% 55%/55% 45% 55% 45%;background:linear-gradient(135deg,#6f9a3c,#2f4a1d)"></div>
<div class="photo" role="img" aria-label="Smiling gardener holding a potted plant" style="left:764px;top:235px;width:136px;height:136px;border-radius:50%;border:5px solid var(--cream);background:linear-gradient(135deg,#9bb36e,#566b3a)"></div>
<div class="deco" role="img" aria-label="Green leaf decoration" style="left:596px;top:292px;width:96px;height:80px"></div>
<div class="deco" role="img" aria-label="Potted plant decoration" style="left:20px;top:606px;width:110px;height:150px"></div>
<div class="deco" role="img" aria-label="Leaf decoration" style="left:1060px;top:140px;width:80px;height:80px"></div>
<div class="deco" role="img" aria-label="Leaves decoration" style="left:1090px;top:630px;width:110px;height:120px"></div>

<!-- Features -->
<section>
  <div class="feature" style="left:102px"><div class="icon-ring"><svg width="26" height="26" viewBox="0 0 24 24" fill="none" stroke="var(--green)" stroke-width="1.6"><path d="M4 20c8 0 14-6 16-16C10 5 4 11 4 20z"/></svg></div><h3>99% Guarantee Services</h3><p>Convenient &amp; proacteds bested quality and ideas use production.</p></div>
  <div class="feature" style="left:353px"><div class="icon-ring"><svg width="26" height="26" viewBox="0 0 24 24" fill="none" stroke="var(--green)" stroke-width="1.6"><path d="M12 21V9M12 13c-4 0-6-3-6-7 4 0 6 3 6 7zM12 11c0-4 2-7 6-7 0 4-2 7-6 7z"/></svg></div><h3>Environmentally Friendly</h3><p>Convenient &amp; proacteds bested quality and ideas use production.</p></div>
  <div class="feature" style="left:606px"><div class="icon-ring"><svg width="26" height="26" viewBox="0 0 24 24" fill="none" stroke="var(--green)" stroke-width="1.6"><path d="M7 13h10l-2 8H9zM12 13V5M12 9l-3-3M12 8l3-3"/></svg></div><h3>Dedicated Support Team</h3><p>Convenient &amp; proacteds bested quality and ideas use production.</p></div>
  <div class="feature" style="left:858px"><div class="icon-ring"><svg width="26" height="26" viewBox="0 0 24 24" fill="none" stroke="var(--green)" stroke-width="1.6"><path d="M4 10h10l4-3v10l-4-3H4zM8 17v3"/></svg></div><h3>Garden Watering</h3><p>Convenient &amp; proacteds bested quality and ideas use production.</p></div>
</section>

<!-- About -->
<div class="abs about-bg"></div>
<div class="photo" role="img" aria-label="Smiling gardener kneeling beside a lawn mower and autumn leaves" style="left:0;top:1150px;width:598px;height:502px;border-radius:0 60% 0 0/0 55% 0 0;background:linear-gradient(135deg,#7e9c4a,#3b5226 60%,#8a5a2c)"></div>
<div class="deco" role="img" aria-label="Leaf outline decoration" style="left:450px;top:1140px;width:120px;height:130px"></div>
<div class="eyebrow" style="left:608px;top:1148px">Welcome To Larchvale Landscaping</div>
<h2 class="sec-title" style="left:608px;top:1166px">Beautiful Garden Is A<br>Work Of Heart.</h2>
<p class="abs" style="left:608px;top:1250px;width:400px">Continually productize compelling quality for packed with elated productize compelling quality for packed in with all elated Them Setting up to website and creating pages.</p>
<div class="checks" style="left:608px;top:1328px">
  <span>Trimming &amp; Pruning</span><span>Peseta &amp; Weeds Control.</span>
  <span>Peseta &amp; Weeds Control.</span><span>Arbor Management</span>
  <span>Nursery / Tree From</span><span>Trimming &amp; Pruning</span>
  <span>Peseta &amp; Weeds Control.</span><span>Nursery / Tree From</span>
</div>
<div class="stat-mini" style="left:608px;top:1462px"><div class="icon-ring"><svg width="22" height="22" viewBox="0 0 24 24" fill="none" stroke="var(--green)" stroke-width="1.6"><path d="M7 12h10l-2 9H9zM12 12V4"/></svg></div><div><strong>653</strong><em>Garden Make</em></div></div>
<div class="stat-mini" style="left:800px;top:1462px"><div class="icon-ring"><svg width="22" height="22" viewBox="0 0 24 24" fill="none" stroke="var(--green)" stroke-width="1.6"><path d="M7 4h10v5a5 5 0 01-10 0zM12 14v5M8 20h8"/></svg></div><div><strong>20</strong><em>Award Wining</em></div></div>
<div class="btn" style="left:608px;top:1546px;width:175px;height:42px">About Our Company</div>
<div class="deco" role="img" aria-label="Garden shears decoration" style="left:1030px;top:1130px;width:130px;height:110px"></div>
<div class="deco" role="img" aria-label="Seedling in pot with garden tools" style="left:980px;top:1410px;width:200px;height:240px"></div>

<!-- Services -->
<div class="eyebrow" style="left:104px;top:1764px">Larchvale Landscaping Services</div>
<h2 class="sec-title" style="left:104px;top:1782px">Larchvale Landscaping Best<br>Services For Gardening.</h2>
<p class="abs" style="left:104px;top:1866px;width:470px">Continually productize compelling quality for packed in business consulting Setting up to website and creating pages.</p>
<div class="service" style="left:104px;top:1944px"><div class="icon-ring"><svg width="24" height="24" viewBox="0 0 24 24" fill="none" stroke="var(--green)" stroke-width="1.6"><path d="M4 20h16M12 20V10M12 14c-4 0-6-3-6-6 4 0 6 3 6 6z"/></svg></div><h3>Garden Plantations</h3><p>Continua productize compel packed productize compelling quality for all creating website pages.</p><a>Read More »</a></div>
<div class="service" style="left:357px;top:1944px"><div class="icon-ring"><svg width="24" height="24" viewBox="0 0 24 24" fill="none" stroke="var(--green)" stroke-width="1.6"><path d="M4 20h16M6 20v-6M12 20v-9M18 20v-6M8 6l4-3 4 3"/></svg></div><h3>Garden Irrigation System</h3><p>Continua productize compel packed productize compelling quality for all creating website pages.</p><a>Read More »</a></div>
<div class="service" style="left:104px;top:2172px"><div class="icon-ring"><svg width="24" height="24" viewBox="0 0 24 24" fill="none" stroke="var(--green)" stroke-width="1.6"><path d="M4 20l8-8M12 12l6-8M12 12l8-2"/></svg></div><h3>Garden Hedge Cutting</h3><p>Continua productize compel packed productize compelling quality for all creating website pages.</p><a>Read More »</a></div>
<div class="service" style="left:357px;top:2172px"><div class="icon-ring"><svg width="24" height="24" viewBox="0 0 24 24" fill="none" stroke="var(--green)" stroke-width="1.6"><path d="M5 20c7 0 13-5 14-14-9 1-14 7-14 14zM9 16l5-5"/></svg></div><h3>Guarantee Design</h3><p>Continua productize compel packed productize compelling quality for all creating website pages.</p><a>Read More »</a></div>
<div class="photo" role="img" aria-label="Hands holding a seedling with soil beside a trowel" style="left:608px;top:1743px;width:395px;height:390px;border-radius:6px;background:linear-gradient(135deg,#a8b08a,#4f5b36)"></div>
<div class="photo" role="img" aria-label="Smiling gardener in an apron holding a potted plant and trowel" style="left:700px;top:1992px;width:396px;height:393px;border-radius:6px;border:6px solid #fff;background:linear-gradient(135deg,#d9dccc,#7f8c63)"></div>
<div class="deco" role="img" aria-label="Seedling pot with tools decoration" style="left:1000px;top:2330px;width:160px;height:150px"></div>

<!-- Counters -->
<div class="abs counters" role="img" aria-label="Dark garden soil background"></div>
<div class="counter" style="left:114px"><div class="icon-ring"></div><strong>5,253</strong><span>Garden Complete</span></div>
<div class="counter" style="left:371px"><div class="icon-ring"></div><strong>6,253</strong><span>Satisfied Clients</span></div>
<div class="counter" style="left:628px"><div class="icon-ring"></div><strong>7,253</strong><span>National Award</span></div>
<div class="counter" style="left:884px"><div class="icon-ring"></div><strong>6,253</strong><span>Team Members</span></div>

<!-- Team -->
<div class="deco" role="img" aria-label="Potted plant decoration" style="left:14px;top:2838px;width:190px;height:150px"></div>
<div class="eyebrow" style="left:534px;top:2892px">Our Team Member</div>
<h2 class="center head" style="top:2908px;font-size:27px;font-weight:600">Our Professional Landscapers</h2>
<p class="center" style="top:2950px;padding:0 410px">Continually productize compelling quality for packed business consulting Setting up to website and creating pages.</p>
<div class="member" style="left:104px"><div class="photo" role="img" aria-label="Gardener trimming a hedge" style="background:linear-gradient(160deg,#7a9b4c,#2f4620)"></div><i class="share"></i><h4>Owen Hartley</h4><span>Gardenist</span></div>
<div class="member" style="left:357px"><div class="photo" role="img" aria-label="Gardener pruning a shrub" style="background:linear-gradient(160deg,#96a97a,#3f5630)"></div><i class="share"></i><h4>Owen Hartley</h4><span>Gardenist</span></div>
<div class="member" style="left:608px"><div class="photo" role="img" aria-label="Gardener with a watering can in a greenhouse" style="background:linear-gradient(160deg,#b3c79a,#4b6b33)"></div><i class="share"></i><h4>Clara Wendell</h4><span>Gardenist</span></div>
<div class="member" style="left:861px"><div class="photo" role="img" aria-label="Gardener carrying a crate of plants" style="background:linear-gradient(160deg,#a4b88b,#52683c)"></div><i class="share"></i><h4>Ivan Morrow</h4><span>Gardenist</span></div>
<div class="btn" style="left:517px;top:3385px;width:166px;height:41px">View All Members</div>
<div class="deco" role="img" aria-label="Flowers in a yellow pot decoration" style="left:980px;top:3330px;width:200px;height:190px"></div>

<!-- Testimonials -->
<div class="photo" role="img" aria-label="Two gardeners holding potted plants in a greenhouse" style="left:0;top:3522px;width:600px;height:743px;background:linear-gradient(135deg,#5f6f4a,#2b3322)"></div>
<div class="abs" style="left:366px;top:3860px;width:54px;height:54px;border-radius:50%;background:var(--green);display:flex;align-items:center;justify-content:center"><svg width="18" height="18" viewBox="0 0 24 24"><path d="M7 4l13 8-13 8z" fill="#fff"/></svg></div>
<div class="abs testi-bg"></div>
<div class="eyebrow" style="left:641px;top:3614px">Our Feedback</div>
<h2 class="sec-title" style="left:641px;top:3632px">What Our Client Say About Us</h2>
<p class="abs" style="left:641px;top:3676px;width:430px">Continually productize compelling quality packed business consulting Setting up to website and creating pages.</p>
<div class="deco" role="img" aria-label="Garden shears decoration" style="left:1050px;top:3560px;width:140px;height:110px"></div>
<div class="review" style="top:3756px;height:181px"><div class="who"><div class="avatar" role="img" aria-label="Client portrait"></div><div><h4>Nadia Fenwick</h4><small>Founder</small></div><div class="stars">★★★★★</div></div><p>Rapaciously simplify enabled intellectual capital and transparent it core competencies energetically enable user centric remarkets the after leveraged methodologies.</p></div>
<div class="review" style="top:3970px;height:189px"><div class="who"><div class="avatar" role="img" aria-label="Client portrait"></div><div><h4>Marcus Pell</h4><small>Manager</small></div><div class="stars">★★★★★</div></div><p>Rapaciously simplify enabled intellectual capital and transparent it core competencies energetically enable user centric remarkets the after leveraged methodologies.</p></div>
<div class="deco" role="img" aria-label="Watering can and potted plants decoration" style="left:1010px;top:4090px;width:180px;height:170px"></div>

<!-- Partners -->
<div class="badge" style="left:148px"></div>
<div class="badge" style="left:345px"></div>
<div class="badge" style="left:543px"></div>
<div class="badge" style="left:742px"></div>
<div class="badge" style="left:939px"></div>

<!-- Footer -->
<footer class="footer">
  <div class="abs footer-bg"></div>
  <div class="deco" role="img" aria-label="Faint leaf decoration" style="left:60px;top:4470px;width:150px;height:120px;opacity:.25"></div>
  <h4 style="left:104px">About Us</h4>
  <p class="abs" style="left:104px;top:4666px;width:240px">We believe that boutique practice are better placed info respond quickly our client bespoke service</p>
  <h4 style="left:104px;top:4742px">Follow Us</h4>
  <div class="abs" style="left:104px;top:4776px;display:flex;gap:10px"><i style="width:24px;height:24px;border-radius:50%;background:var(--ink)"></i><i style="width:24px;height:24px;border-radius:50%;background:var(--ink)"></i><i style="width:24px;height:24px;border-radius:50%;background:var(--ink)"></i><i style="width:24px;height:24px;border-radius:50%;background:var(--ink)"></i></div>
  <h4 style="left:400px">Quick Links</h4>
  <ul class="links"><li>Garden Services</li><li>About Company</li><li>Garden Projects</li><li>Team Member</li><li>Contact us</li></ul>
  <h4 style="left:608px">Recent News</h4>
  <div class="news" style="top:4664px"><div class="photo" role="img" aria-label="Gardener tending plants" style="background:linear-gradient(135deg,#8aa06a,#44572f)"></div><div><b>How To Clean Your Fast More Efficiently.</b><span>14 July 2025</span></div></div>
  <div class="news" style="top:4752px"><div class="photo" role="img" aria-label="Gardener in a greenhouse" style="background:linear-gradient(135deg,#9db281,#4d6238)"></div><div><b>How To Clean Your Fast More Efficiently.</b><span>14 July 2025</span></div></div>
  <h4 style="left:861px">Photo Gallery</h4>
  <div class="gallery" role="img" aria-label="Six garden work photos"><div></div><div></div><div></div><div></div><div></div><div></div></div>
  <div class="abs copy-line"></div>
  <p class="center copy">© Copyright 2025. All Rights Reserved</p>
</footer>

</body>
</html>
```